Website for UK Fintech Company specialising in Auto-Finance asset management

We need a website for a FINTECH business called KELP Asset Management. We have developed and licenced an innovative platform to provide financial institutions whom provide secured Asset finance loans to consumer and commercial clients, allowing for real time tracking and management of defaulted accounts pending repossession. The KELP Asset Management platform is a total recoveries solution through the cycle, from the moment the lender has to recover the vehicle (due to default/non-payment) to the disposal of the vehicle (via sale at Motor Auctions or by selling to a Car dealership network). The data provided from external services allows the Financier to make informed decisions, such as whether it is economical to continue the recovery and decide which sales channel is better suited for their assets to maximise residual values and minimise financial losses. The KELP platform provides an array of MI reporting and uses a systematic approach utilising exception reporting to identify key areas of non-performance to enable focus where needed. KELP also provides a leading Debt collection service recovering end-of-cycle losses such as Financial Shortfall and losses in vehicle values due to conditions and excessive damage.

We also require a new logo for out new product called MB-Prismo

Target Market(s)

Financial institutions whom provide secured Asset finance loans to consumer and commercial clients

Industry/Entity Type

Financial Service

Logo Text

MB- Prismo (this is for a new product which forms part of the KELP Asset Mangement Platform

Number of Pages Required

4 page

Font styles to use
Serif
Sans Serif

Colors

Designer to choose colors to be used in the design.

Requirements
Must have
• We need a simple website with a broken down as follows;
• • Landing page
• • Services page
• • About us page
• • KELP Asset Management Platform login page (client facing)
Nice to have
• Our slogan is 'Auto-Finance Expertise'
• We are very much open to suggestions as long as we can create a professional/ corporate / modern feel to the website. We are a FINTECH company, and that needs to come across
Should not have
• Whilst we are an asset management company primarily managing vehicles through our platform, we don't want it to look like a car dealership website!:)

```html
<!DOCTYPE html>
<html lang="en">
<head>
<meta charset="utf-8">
<title>KELP Asset Management Platform</title>
<link rel="stylesheet" href="https://fonts.googleapis.com/css2?family=Roboto:wght@300;400;500;700&display=swap">
<style>
:root{
  --orange:#f07d00;
  --ink:#1d1d1d;
  --text:#555;
  --muted:#777;
  --card:#f1f1f1;
  --card-line:#e2e2e2;
  --band:#f3f0eb;
  --footer:#272727;
  --white:#fff;
}
*{margin:0;padding:0;box-sizing:border-box}
html,body{width:1200px;height:3435px;overflow:hidden}
body{font-family:"Roboto",Arial,sans-serif;color:var(--text);background:var(--white);position:relative}
a{color:inherit;text-decoration:none}
.wrap{width:980px;margin:0 auto;position:relative}
.btn{display:inline-block;background:var(--orange);color:var(--white);font-size:11px;padding:6px 12px;border-radius:2px}
.btn-outline{display:inline-block;border:2px solid var(--orange);color:var(--orange);font-size:12px;font-weight:700;letter-spacing:.5px;padding:9px 26px;border-radius:20px;text-transform:uppercase;background:var(--white)}

/* header */
.site-header{height:92px;display:flex;align-items:center;justify-content:space-between;padding:0 110px}
.brand{display:flex;flex-direction:column}
.brand-name{font-size:34px;font-weight:700;color:var(--ink);line-height:1}
.brand-tag{font-size:8px;font-weight:700;color:var(--orange);letter-spacing:.3px;margin-top:3px}
.main-nav{display:flex;align-items:center;gap:30px;font-size:13px;font-weight:500;color:var(--ink);text-transform:uppercase}
.main-nav .active{color:var(--orange)}
.nav-phone{display:flex;align-items:center;gap:6px;font-weight:700}
.nav-login{background:var(--orange);color:var(--white);padding:9px 30px;font-weight:700;font-size:12px}

/* hero */
.hero{height:515px;position:relative;background:linear-gradient(100deg,#9a9a98 0%,#6f6d6b 35%,#3c3f48 60%,#27324a 85%,#1f2a40 100%);text-align:center;color:var(--white)}
.hero-content{position:absolute;top:188px;left:0;right:0}
.hero h1{font-size:32px;font-weight:700;text-shadow:0 2px 4px rgba(0,0,0,.35)}
.hero p{font-size:13px;margin-top:8px}
.hero-actions{margin-top:38px;display:flex;justify-content:center;gap:14px}
.hero-actions a{font-size:11px;font-weight:700;text-transform:uppercase;padding:10px 26px;border-radius:20px;letter-spacing:.4px}
.hero-ghost{border:2px solid var(--white)}
.hero-solid{background:var(--orange);border:2px solid var(--orange)}

/* welcome */
.welcome{height:339px;text-align:center;padding-top:62px;border-bottom:1px solid #eee}
.welcome h2{font-size:42px;font-weight:400;color:var(--ink)}
.welcome h2 b{font-weight:700}
.welcome h2 span{color:var(--orange)}
.welcome .lead{font-size:15px;color:var(--ink);margin-top:2px}
.welcome .body{font-size:12px;line-height:21px;color:var(--muted);width:770px;margin:22px auto 0}
.welcome .btn-outline{margin-top:22px}

/* section title */
.section-title{text-align:center}
.section-title h2{font-size:36px;font-weight:500;color:var(--ink)}
.section-title p{font-size:15px;color:var(--ink);margin-top:4px}

/* products */
.products{height:611px;padding-top:42px}
.product-grid{margin-top:44px;display:grid;grid-template-columns:repeat(3,1fr);background:var(--card);border:1px solid var(--card-line)}
.product{height:180px;text-align:center;padding:40px 28px 0;border-right:1px solid var(--card-line);border-bottom:1px solid var(--card-line)}
.product:nth-child(3n){border-right:none}
.product:nth-child(n+4){border-bottom:none}
.product h3{font-size:16px;font-weight:500;color:var(--ink)}
.product p{font-size:11.5px;line-height:20px;color:var(--muted);margin:14px 0 10px}

/* benefits */
.benefits{height:408px;display:flex;gap:23px}
.benefits-photo{width:478px;height:348px;background:linear-gradient(135deg,#d9dde0,#b9c4cc 50%,#8aa3b5);flex:none}
.benefits h2{font-size:36px;font-weight:500;color:var(--ink);margin-top:20px}
.benefit-list{list-style:none;margin-top:22px}
.benefit-list li{display:flex;align-items:center;gap:14px;font-size:12px;color:var(--muted);height:31px}

/* new product */
.new-product{height:213px;background:var(--band);display:flex;align-items:center}
.new-product .wrap{display:flex;align-items:center;justify-content:space-between}
.new-product h2{font-size:36px;font-weight:500;color:var(--ink)}
.new-product p{font-size:12px;line-height:21px;color:var(--muted);width:650px;margin-top:10px}
.product-name{font-size:38px;font-weight:700;color:var(--ink);margin-right:28px}

/* about cards */
.know-us{height:570px;padding-top:50px}
.card-row{display:flex;gap:24px;margin-top:36px}
.info-card{width:311px;height:408px;background:var(--card);text-align:center}
.info-card .photo{height:199px}
.info-card h3{font-size:16px;font-weight:500;color:var(--ink);margin-top:28px}
.info-card p{font-size:11.5px;line-height:20px;color:var(--muted);padding:0 30px;margin:12px 0 12px}

/* help */
.help{height:359px;text-align:center;padding-top:72px}
.help-title{display:flex;align-items:center;gap:22px}
.help-title hr{flex:1;border:none;border-top:2px solid var(--ink)}
.help-title h2{font-size:36px;font-weight:500;color:var(--ink)}
.help p{font-size:13px;line-height:22px;color:var(--muted);margin-top:12px}
.help .btn-outline{margin-top:20px;font-size:11px}

/* footer */
.site-footer{height:328px;background:var(--footer);color:#ddd;position:relative}
.footer-cols{position:absolute;top:50px;left:110px;right:110px;display:flex}
.footer-col h4{font-size:11px;font-weight:700;color:var(--white);text-transform:uppercase;margin-bottom:14px}
.footer-col li{list-style:none;font-size:11.5px;line-height:24px}
.footer-col address{font-style:normal;font-size:11.5px;line-height:18px}
.col-links{width:142px}.col-services{width:199px}.col-info{width:160px}.col-contact{width:252px}
.col-news{width:228px}
.news-input{height:36px;border-radius:18px;background:var(--white);color:#999;font-size:11px;padding:11px 20px}
.news-btn{height:34px;border-radius:17px;background:var(--orange);color:var(--white);font-size:11px;font-weight:700;text-align:center;line-height:34px;margin-top:9px;text-transform:uppercase}
.social{display:flex;gap:8px;margin-top:8px}
.social i{width:28px;height:28px;border:2px solid var(--white);border-radius:50%}
.copyright{position:absolute;left:110px;top:264px;font-size:11.5px}
.chat-tab{position:absolute;right:110px;bottom:0;width:243px;height:35px;background:var(--orange);border-radius:8px 8px 0 0;color:var(--white);font-size:11px;font-weight:700;display:flex;align-items:center;justify-content:center;gap:8px;text-transform:uppercase}
</style>
</head>
<body>

<header class="site-header">
  <div class="brand">
    <div class="brand-name">KELP</div>
    <div class="brand-tag">ASSET MANAGEMENT PLATFORM</div>
  </div>
  <nav class="main-nav">
    <a class="active" href="#">Home</a>
    <a href="#">Services</a>
    <a href="#">About</a>
    <a href="#">Blog</a>
    <a href="#">Contact</a>
    <span class="nav-phone">
      <svg width="13" height="13" viewBox="0 0 24 24"><path fill="#1d1d1d" d="M6.6 10.8a15.1 15.1 0 0 0 6.6 6.6l2.2-2.2c.3-.3.7-.4 1-.2 1.1.4 2.3.6 3.6.6.6 0 1 .4 1 1V20c0 .6-.4 1-1 1A17 17 0 0 1 3 4c0-.6.4-1 1-1h3.5c.6 0 1 .4 1 1 0 1.3.2 2.5.6 3.6.1.3 0 .7-.2 1z"/></svg>
      +44 (0)20 7946 0321
    </span>
    <a class="nav-login" href="#">Login</a>
  </nav>
</header>

<section class="hero" role="img" aria-label="Businessman in a suit with a city skyline and rising financial chart overlay">
  <div class="hero-content">
    <h1>The Rise Of Fintech In Asset Management Platform</h1>
    <p>Lorem ipsum dolor sit amet, consectetur adipiscing elit, sed do eiusmod tempor incididunt ut labore et dolore magna aliqua. Ut enim ad</p>
    <div class="hero-actions">
      <a class="hero-ghost" href="#">Explore Services</a>
      <a class="hero-solid" href="#">Contact Us Today!</a>
    </div>
  </div>
</section>

<section class="welcome">
  <h2>Welcome to <b>KELP</b> <span>Asset Management Platform</span></h2>
  <p class="lead">Lorem ipsum dolor sit amet, consectetur adipiscing elit</p>
  <p class="body">Sed non mauris vitae erat consequat auctor eu in elit. Class aptent taciti sociosqu ad litora torquent per conubia nostra, per inceptos himenaeos. Mauris in erat justo. Nullam ac urna eu felis dapibus condimentum sit amet a augue. Sed non neque elit. Sed ut imperdiet nisi. Proin condimentum fermentum nunc. Etiam pharetra, erat sed fermentum feugiat, velit mauris egestas quam, ut aliquam massa nisl quis neque. Suspendisse in orci enim.</p>
  <a class="btn-outline" href="#">Explore Services</a>
</section>

<section class="products">
  <div class="wrap">
    <div class="section-title">
      <h2>AssistKelp Products</h2>
      <p>Suspendisse sollicitudin mi quis mi dictum, a condimentum lectus placerat.</p>
    </div>
    <div class="product-grid">
      <div class="product"><h3>Sed ultricies velit tristique</h3><p>Sed non mauris vitae erat consequat auctor eu in elit. Class aptent taciti sociosqu ad litora torquent per conubia nostra.</p><a class="btn" href="#">Read More</a></div>
      <div class="product"><h3>Interdum justo sed, pretium massa</h3><p>Sed non mauris vitae erat consequat auctor eu in elit. Class aptent taciti sociosqu ad litora torquent per conubia nostra.</p><a class="btn" href="#">Read More</a></div>
      <div class="product"><h3>Proin sodales purus</h3><p>Sed non mauris vitae erat consequat auctor eu in elit. Class aptent taciti sociosqu ad litora torquent per conubia nostra.</p><a class="btn" href="#">Read More</a></div>
      <div class="product"><h3>Aenean dictum ante</h3><p>Sed non mauris vitae erat consequat auctor eu in elit. Class aptent taciti sociosqu ad litora torquent per conubia nostra.</p><a class="btn" href="#">Read More</a></div>
      <div class="product"><h3>Curabitur scelerisque magna</h3><p>Sed non mauris vitae erat consequat auctor eu in elit. Class aptent taciti sociosqu ad litora torquent per conubia nostra.</p><a class="btn" href="#">Read More</a></div>
      <div class="product"><h3>Praesent id ligula consectetur</h3><p>Sed non mauris vitae erat consequat auctor eu in elit. Class aptent taciti sociosqu ad litora torquent per conubia nostra.</p><a class="btn" href="#">Read More</a></div>
    </div>
  </div>
</section>

<section class="wrap benefits">
  <div class="benefits-photo" role="img" aria-label="Three colleagues reviewing documents together at an office desk"></div>
  <div>
    <h2>What Are The Benefits?</h2>
    <ul class="benefit-list">
      <li><svg width="12" height="8" viewBox="0 0 12 8"><path d="M0 4h10M7 1l3 3-3 3" stroke="#777" fill="none"/></svg>Lorem ipsum dolor sit amet, consectetur adipiscing elit.</li>
      <li><svg width="12" height="8" viewBox="0 0 12 8"><path d="M0 4h10M7 1l3 3-3 3" stroke="#777" fill="none"/></svg>Suspendisse sollicitudin mi quis mi dictum, a condimentum lectus placerat.</li>
      <li><svg width="12" height="8" viewBox="0 0 12 8"><path d="M0 4h10M7 1l3 3-3 3" stroke="#777" fill="none"/></svg>Sed ultricies velit tristique, interdum justo sed, pretium massa.</li>
      <li><svg width="12" height="8" viewBox="0 0 12 8"><path d="M0 4h10M7 1l3 3-3 3" stroke="#777" fill="none"/></svg>Curabitur convallis lectus vitae tortor convallis facilisis.</li>
      <li><svg width="12" height="8" viewBox="0 0 12 8"><path d="M0 4h10M7 1l3 3-3 3" stroke="#777" fill="none"/></svg>Quisque molestie sapien id placerat sodales.</li>
      <li><svg width="12" height="8" viewBox="0 0 12 8"><path d="M0 4h10M7 1l3 3-3 3" stroke="#777" fill="none"/></svg>Aenean mattis est quis neque varius, vitae dapibus augue luctus.</li>
      <li><svg width="12" height="8" viewBox="0 0 12 8"><path d="M0 4h10M7 1l3 3-3 3" stroke="#777" fill="none"/></svg>Sed ultricies velit tristique, interdum justo sed, pretium massa.</li>
      <li><svg width="12" height="8" viewBox="0 0 12 8"><path d="M0 4h10M7 1l3 3-3 3" stroke="#777" fill="none"/></svg>Curabitur convallis lectus vitae tortor convallis facilisis.</li>
    </ul>
  </div>
</section>

<section class="new-product">
  <div class="wrap">
    <div>
      <h2>New Product</h2>
      <p>Sed non mauris vitae erat consequat auctor eu in elit. Class aptent taciti sociosqu ad litora torquent per conubia nostra, per inceptos himenaeos. Mauris in erat justo. Nullam ac urna eu felis dapibus condimentum sit amet a augue. Sed non neque elit. Sed ut imperdiet nisi. Proin condimentum fermentum nunc. Etiam pharetra, erat sed fermentum feugiat, velit mauris egestas quam, ut aliquam massa nisl quis neque. Suspendisse in orci enim.</p>
    </div>
    <div class="product-name">MB-Prismo</div>
  </div>
</section>

<section class="know-us">
  <div class="wrap">
    <div class="section-title">
      <h2>Know Us Better</h2>
      <p>Suspendisse sollicitudin mi quis mi dictum, a condimentum lectus placerat.</p>
    </div>
    <div class="card-row">
      <div class="info-card">
        <div class="photo" role="img" aria-label="Senior couple reviewing finances on a laptop at home" style="background:linear-gradient(135deg,#c9c2b6,#9d9386 60%,#6f7f95)"></div>
        <h3>Quisque molestie sapien</h3>
        <p>Sed non mauris vitae erat consequat auctor eu in elit. Class aptent taciti sociosqu ad litora torquent per conubia nostra.</p>
        <a class="btn" href="#">Read More</a>
      </div>
      <div class="info-card">
        <div class="photo" role="img" aria-label="Desk with calculator, financial charts and reports" style="background:linear-gradient(135deg,#9fd3dc,#5fb6c6 55%,#3d8fa6)"></div>
        <h3>Quisque molestie sapien</h3>
        <p>Sed non mauris vitae erat consequat auctor eu in elit. Class aptent taciti sociosqu ad litora torquent per conubia nostra.</p>
        <a class="btn" href="#">Read More</a>
      </div>
      <div class="info-card">
        <div class="photo" role="img" aria-label="Couple shaking hands with an advisor in a bright modern home" style="background:linear-gradient(135deg,#e4e6e8,#b8c2cc 55%,#7b8a99)"></div>
        <h3>Quisque molestie sapien</h3>
        <p>Sed non mauris vitae erat consequat auctor eu in elit. Class aptent taciti sociosqu ad litora torquent per conubia nostra.</p>
        <a class="btn" href="#">Read More</a>
      </div>
    </div>
  </div>
</section>

<section class="help">
  <div class="wrap">
    <div class="help-title"><hr><h2>How Can We help You?</h2><hr></div>
    <p>We ready to help you. Give us a call or fill out this form to request service or ask a question about it.<br>We look forward to visiting with you!</p>
    <a class="btn-outline" href="#">Contact Us Today!</a>
  </div>
</section>

<footer class="site-footer">
  <div class="footer-cols">
    <div class="footer-col col-links">
      <h4>Quick Links</h4>
      <ul><li>Home</li><li>Services</li><li>About</li><li>Blog</li><li>Contact</li></ul>
    </div>
    <div class="footer-col col-services">
      <h4>Services</h4>
      <ul><li>Lorem ipsum dolor</li><li>Lorem ipsum dolor</li><li>Lorem ipsum dolor</li><li>Lorem ipsum dolor</li><li>Lorem ipsum dolor</li></ul>
    </div>
    <div class="footer-col col-info">
      <h4>Information</h4>
      <ul><li>Terms of Use</li><li>Privacy Policy</li></ul>
    </div>
    <div class="footer-col col-contact">
      <h4>Contact Us</h4>
      <address>KELP Asset Management Platform<br>229, Lorem Ipsum dolor sit,<br>dosis amet sit 54859<br><br>T: +44 (0)20 7946 0321<br>E: info@kelpasset.co.uk</address>
    </div>
    <div class="footer-col col-news">
      <h4>Subscribe Newsletter</h4>
      <div class="news-input">Email Address</div>
      <div class="news-btn">Subscribe Now!</div>
      <h4 style="margin:16px 0 0">We're Social</h4>
      <div class="social"><i></i><i></i><i></i></div>
    </div>
  </div>
  <p class="copyright">©2018 KELP Asset Management Platform.</p>
  <div class="chat-tab">
    <svg width="14" height="13" viewBox="0 0 14 13"><path d="M1 1h12v8H6l-3 3V9H1z" fill="#fff"/></svg>
    Need to help? Live chat now!
  </div>
</footer>

</body>
</html>
```